Simple Modern Label for a Coconut oil product

We need a label designed for Organic Coconut oil. We would like the label to convey the gourmet/high quality product. It should be modern and simple and look like an artisinal product. The label will need to contain all the basic label requirements - Independence list, place for nutrition facts, our company logo etc.
The label will ultimately be printed as oil proof, so it will have a glossy appearance.
I have includes some examples that I like and a file with the logo.

Product Container - Wide Mount Clear Glass Jar: 4.75 inches tall (base to the bottom of the lid) and 9.5 in circumference
Label: Can be 1 or 2 separate labels, round, square and rectangle are okay
No larger than 3 inches high and 9 inches long

Target Market(s)

Middle Age home chef

Industry/Entity Type

Product

Requirements
Must have
• - logo (Attached below, I have this in multiple formats, let me know if you need them)
• - 14 FL OZ (414mL)
• - ingredient: organic unrefined whole kernel virgin coconut oil,
• - Manufacturer: XXX Y St., anywhere, CA, 99999
• - Distributed by Meadowfern Naturals, P.O. Box 5521, Oakland, CA 94612 www.MeadowfernNaturals.example
• - Certified Organic by Company Name
• - Product of Sri Lanka
Nice to have
• - Nutrition Facts
Should not have
• Clutter

```html
<!DOCTYPE html>
<html lang="en">
<head>
<meta charset="utf-8">
<title>Meadowfern Naturals – Organic Unrefined Coconut Oil Label</title>
<link href="https://fonts.googleapis.com/css2?family=Montserrat:wght@300;500&display=swap" rel="stylesheet">
<style>
  :root {
    --page: #ffffff;
    --cream: #f6f3dc;
    --leaf-dark: #2f6a14;
    --leaf: #4c8f1f;
    --leaf-light: #7bb53a;
    --band: #15131f;
    --ink-light: #ffffff;
  }
  html, body {
    margin: 0;
    width: 1200px;
    height: 1200px;
    overflow: hidden;
    background: var(--page);
    font-family: "Montserrat", sans-serif;
  }
  .label {
    position: absolute;
    left: 60px;
    top: 115px;
    width: 1080px;
    height: 970px;
    overflow: hidden;
    background: var(--cream);
  }
  .label__art {
    position: absolute;
    inset: 0;
    background:
      radial-gradient(ellipse 60% 45% at 45% 18%, var(--leaf) 0%, var(--leaf-dark) 45%, transparent 75%),
      radial-gradient(ellipse 35% 40% at 88% 55%, var(--leaf-light) 0%, var(--leaf) 40%, transparent 75%),
      radial-gradient(ellipse 40% 30% at 55% 92%, var(--leaf) 0%, var(--leaf-dark) 40%, transparent 75%),
      var(--cream);
  }
  .label__band {
    position: absolute;
    left: 0;
    top: 394px;
    width: 796px;
    height: 360px;
    background: var(--band);
    color: var(--ink-light);
  }
  .brand {
    position: absolute;
    left: 50px;
    top: 70px;
    width: 200px;
    text-align: center;
  }
  .brand__mark {
    display: block;
    width: 70px;
    height: 70px;
    margin: 0 auto 22px;
    border-radius: 50%;
    background: var(--ink-light);
  }
  .brand__name {
    font-weight: 500;
    font-size: 22px;
    line-height: 28px;
    letter-spacing: 1px;
    text-transform: uppercase;
  }
  .volume {
    position: absolute;
    right: 556px;
    top: 250px;
    text-align: right;
    font-weight: 300;
    font-size: 15px;
    line-height: 22px;
    letter-spacing: 1px;
  }
  .volume__rule {
    display: block;
    width: 12px;
    height: 1px;
    margin: 6px 0 6px auto;
    background: var(--ink-light);
  }
  .divider {
    position: absolute;
    left: 272px;
    top: 38px;
    width: 3px;
    height: 286px;
    background: var(--ink-light);
  }
  .product-name {
    position: absolute;
    left: 306px;
    top: 36px;
    margin: 0;
    font-size: 60px;
    line-height: 72px;
    letter-spacing: 2px;
    text-transform: uppercase;
  }
  .product-name__light { display: block; font-weight: 300; }
  .product-name__strong { display: block; font-weight: 500; }
</style>
</head>
<body>
  <div class="label">
    <div class="label__art" role="img" aria-label="Botanical illustration of a coconut palm crown with green fronds and coconuts on a cream background"></div>
    <div class="label__band">
      <div class="brand">
        <span class="brand__mark"></span>
        <div class="brand__name">Meadowfern Naturals</div>
      </div>
      <div class="volume">14 FL OZ<span class="volume__rule"></span>414 ML</div>
      <div class="divider"></div>
      <h1 class="product-name">
        <span class="product-name__light">Organic</span>
        <span class="product-name__light">Unrefined</span>
        <span class="product-name__strong">Coconut</span>
        <span class="product-name__strong">Oil</span>
      </h1>
    </div>
  </div>
</body>
</html>
```